Natural Supplement Co Needs Label Makeover

Our company's success began with our main product, an amino acid blend that aids in fat metabolism, called Vantorel. Since then we continue to expand the product line that now includes a detox called Vantopure, and probiotic called Vantoflora, as well as 3 others, for a total of 6 products/ labels.
Our original design/logo had more of an 'old-timey' feel (see attached 2-product photo). We are looking for a fresh label design update for the product line which reflects the range of supplements as cohesive and individual parts of an overall health plan/strategy (see attached 'Logo Update Test' as just one idea we had in-house, you need not consider it as a starting point).

Target Market(s)

women 25-45

Industry/Entity Type

Health And Wellness

Requirements
Must have
• consistent theme with confident look
Nice to have
• Each product (ie. "Vantorel") has a few-word descriptor: ("Fat-Burning Amino Acids") that should be planned on including as part of each label.
Should not have
• NO 'streamlined' or graphic interpretations of the human body, or figurative image

```html
<!DOCTYPE html>
<html lang="en">
<head>
<meta charset="utf-8">
<title>Vanto Products – Label Line</title>
<link href="https://fonts.googleapis.com/css2?family=Quicksand:wght@300;400;500&display=swap" rel="stylesheet">
<style>
  :root {
    --page: #ffffff;
    --label-light: #ececec;
    --label-light-edge: #d6d6d6;
    --label-dark: #6a6a6a;
    --label-dark-deep: #575757;
    --stripe: #9a9a9a;
    --ink: #3c3c3c;
    --ink-soft: #bdbdbd;
    --white: #ffffff;
    --drops: #7d3a8c;
    --omega: #d7bd1f;
    --flora: #2a9a3c;
    --pure: #2f7fb0;
  }
  * { box-sizing: border-box; margin: 0; padding: 0; }
  html, body { width: 1200px; height: 925px; overflow: hidden; background: var(--page); }
  body { font-family: "Quicksand", sans-serif; color: var(--ink); }

  .label-line {
    position: absolute;
    left: 40px; top: 470px;
    display: flex; gap: 20px;
  }
  .label {
    position: relative;
    width: 170px; height: 230px;
    overflow: hidden;
    box-shadow: 0 6px 14px rgba(0,0,0,0.12);
  }
  .label__top {
    position: absolute; left: 0; top: 0; width: 100%; height: 98px;
    background: linear-gradient(90deg, var(--label-light-edge), var(--label-light) 30%, var(--white) 55%, var(--label-light) 80%, var(--label-light-edge));
  }
  .label__stripe {
    position: absolute; left: 0; top: 98px; width: 100%; height: 6px;
    background: var(--stripe);
  }
  .label__bottom {
    position: absolute; left: 0; top: 110px; width: 100%; height: 120px;
    background: linear-gradient(90deg, var(--label-dark-deep), var(--label-dark) 40%, var(--label-dark) 60%, var(--label-dark-deep));
  }
  .label__gap {
    position: absolute; left: 0; top: 104px; width: 100%; height: 6px;
    background: var(--white);
  }

  .brand {
    position: absolute; top: 14px; width: 100%;
    text-align: center;
    font-size: 17px; font-weight: 400; line-height: 1.05;
    color: var(--ink);
  }
  .product-dot {
    position: absolute; left: 50%; top: 64px;
    width: 68px; height: 68px; margin-left: -34px;
    border-radius: 50%;
    border: 5px solid var(--white);
    box-shadow: 0 0 0 2px var(--label-light-edge);
  }
  .product-dot--drops { background: var(--drops); }
  .product-dot--omega { background: var(--omega); }
  .product-dot--flora { background: var(--flora); }
  .product-dot--pure  { background: var(--pure); }

  .product-name {
    position: absolute; top: 150px; width: 100%;
    text-align: center;
    font-size: 19px; font-weight: 300; color: var(--white);
  }
  .descriptor {
    position: absolute; top: 186px; width: 100%;
    text-align: center;
    font-size: 8px; font-weight: 400; color: var(--ink-soft);
  }

  .fine-print {
    position: absolute;
    font-size: 7px; line-height: 1.45; font-weight: 500;
  }
  .fine-print--ingredients { left: 12px; top: 12px; width: 140px; color: var(--ink); }
  .fine-print--warning { left: 12px; top: 122px; width: 120px; color: var(--white); }
  .fine-print--attention { right: 12px; top: 12px; width: 110px; text-align: center; color: var(--ink); }
  .fine-print strong { font-weight: 500; font-style: italic; }
</style>
</head>
<body>
  <main class="label-line">

    <section class="label label--back-ingredients">
      <div class="label__top"></div>
      <div class="label__stripe"></div>
      <div class="label__gap"></div>
      <div class="label__bottom"></div>
      <p class="fine-print fine-print--ingredients">
        Ingredients: Sweet Almond, Grape Seed, Apricot Seed, Jojoba, Rosehip and Argan Oils. Essential Oils: Fir Needle, Rosemary, Lavender, Cedarwood, Amber, Frankincense, and Vanilla.
      </p>
      <p class="fine-print fine-print--warning">
        Caution: May cause skin irritation. Test a small amount on skin first before using. If your skin reacts, stop use immediately.
      </p>
    </section>

    <section class="label label--back-attention">
      <div class="label__top"></div>
      <div class="label__stripe"></div>
      <div class="label__gap"></div>
      <div class="label__bottom"></div>
      <p class="fine-print fine-print--attention">
        <strong>Attention:</strong> May cause skin irritation. Test a small amount on skin before going too far. If your skin reacts, stop use immediately.
      </p>
    </section>

    <section class="label">
      <div class="label__top"></div>
      <div class="label__stripe"></div>
      <div class="label__gap"></div>
      <div class="label__bottom"></div>
      <p class="brand">Vanto<br>Products</p>
      <div class="product-dot product-dot--drops"></div>
      <h2 class="product-name">Vantorel</h2>
      <p class="descriptor">Fat-Burning Amino Acids</p>
    </section>

    <section class="label">
      <div class="label__top"></div>
      <div class="label__stripe"></div>
      <div class="label__gap"></div>
      <div class="label__bottom"></div>
      <p class="brand">Vanto<br>Products</p>
      <div class="product-dot product-dot--omega"></div>
      <h2 class="product-name">Vantomega</h2>
      <p class="descriptor">Fat-Burning Amino Acids</p>
    </section>

    <section class="label">
      <div class="label__top"></div>
      <div class="label__stripe"></div>
      <div class="label__gap"></div>
      <div class="label__bottom"></div>
      <p class="brand">Vanto<br>Products</p>
      <div class="product-dot product-dot--flora"></div>
      <h2 class="product-name">Vantoflora</h2>
      <p class="descriptor">Fat-Burning Amino Acids</p>
    </section>

    <section class="label">
      <div class="label__top"></div>
      <div class="label__stripe"></div>
      <div class="label__gap"></div>
      <div class="label__bottom"></div>
      <p class="brand">Vanto<br>Products</p>
      <div class="product-dot product-dot--pure"></div>
      <h2 class="product-name">Vantopure</h2>
      <p class="descriptor">Fat-Burning Amino Acids</p>
    </section>

  </main>
</body>
</html>
```